Gymnastics Award Design Needed--for kids

Need a gymnastics certificate or award designed. Will be printed on a piece of 8.5x11 paper. The award will be celebrating the gymnast learning a new skill in gymnastics. So it should be fun, but still look "official". Needs to look good hanging on a gymnast's bedroom wall.

It should say "The Aerial Cartwheel Club"
I will be using this design to change it based on the skill.

My main colors are:
#34475D
#E1467A
#7555A4

So should use those, but can add others

My website is tumblenest.net so you can see the look/feel.

Target Market(s)

Main audience will be girls ages 5-12, but will also be used by slightly older girls and boys. So needs to be fun, not too gender specific.

Industry/Entity Type

Learning

Requirements
Must have
• The following will need to go on the certificate:
• * Name of Skill
• * Image of Skill
• * Gymnast's Name
• * my logo
• * Gym's Logo
• * Gym's Name
• Optional: Date

```html
<!DOCTYPE html>
<html lang="en">
<head>
<meta charset="utf-8">
<title>The Aerial Cartwheel Club – Certificate</title>
<link href="https://fonts.googleapis.com/css2?family=Montserrat:wght@300;400;600;800&display=swap" rel="stylesheet">
<style>
  :root {
    --crimson: #c0213f;
    --rose: #e8467a;
    --salmon: #f4968a;
    --blush: #f7b7c8;
    --blush-light: #fde3ea;
    --ink: #222326;
    --rule: #c9c9cc;
    --purple: #7555a4;
    --paper: #ffffff;
    --figure-tone: #f6c9a8;
    --leotard: #f0607a;
  }
  html, body {
    margin: 0;
    padding: 0;
    overflow: hidden;
    background: var(--paper);
  }
  .certificate {
    position: relative;
    width: 1200px;
    height: 925px;
    overflow: hidden;
    background: var(--paper);
    font-family: "Montserrat", sans-serif;
  }
  .backdrop {
    position: absolute;
    inset: 0;
  }
  .award-ribbon {
    position: absolute;
    left: 79px;
    top: 0;
  }
  .club-title {
    position: absolute;
    left: 0;
    top: 96px;
    width: 1200px;
    margin: 0;
    text-align: center;
    font-weight: 800;
    font-size: 63px;
    line-height: 77px;
    color: var(--crimson);
    letter-spacing: 1px;
  }
  .skill-illustration {
    position: absolute;
    left: 330px;
    top: 259px;
    width: 548px;
    height: 193px;
    border-radius: 6px;
    background: linear-gradient(90deg, var(--blush-light), var(--blush) 50%, var(--blush-light));
  }
  .ground-line {
    position: absolute;
    left: 322px;
    top: 453px;
    width: 556px;
    height: 3px;
    background: var(--rule);
  }
  .presented-band {
    position: absolute;
    left: 315px;
    top: 535px;
    width: 564px;
    height: 38px;
    background: var(--salmon);
    color: var(--paper);
    font-weight: 400;
    font-size: 17px;
    letter-spacing: 0.6px;
    line-height: 38px;
    text-align: center;
  }
  .gymnast-name {
    position: absolute;
    left: 315px;
    top: 618px;
    width: 585px;
    margin: 0;
    text-align: center;
    font-weight: 600;
    font-size: 50px;
    line-height: 60px;
    color: var(--rose);
    letter-spacing: 1px;
  }
  .name-rule {
    position: absolute;
    left: 315px;
    top: 677px;
    width: 585px;
    height: 1px;
    background: var(--rule);
  }
  .award-details {
    position: absolute;
    left: 300px;
    top: 697px;
    width: 615px;
    margin: 0;
    text-align: center;
    font-weight: 400;
    font-size: 26px;
    line-height: 36px;
    color: var(--ink);
  }
  .gym-logo {
    position: absolute;
    left: 153px;
    top: 800px;
    margin: 0;
    font-weight: 600;
    font-size: 33px;
    line-height: 40px;
    color: var(--ink);
  }
  .brand-mark {
    position: absolute;
    left: 750px;
    top: 794px;
    display: flex;
    align-items: center;
    gap: 14px;
  }
  .brand-dot {
    width: 40px;
    height: 40px;
    border-radius: 50%;
    background: var(--purple);
  }
  .brand-name {
    font-weight: 400;
    font-size: 38px;
    line-height: 46px;
    letter-spacing: 1px;
    color: var(--rose);
  }
</style>
</head>
<body>
<main class="certificate">
  <svg class="backdrop" width="1200" height="925" viewBox="0 0 1200 925" aria-hidden="true">
    <defs>
      <linearGradient id="shard-top" x1="0" y1="0" x2="1" y2="1">
        <stop offset="0" stop-color="#f7a3bb"/>
        <stop offset="1" stop-color="#fde3ea" stop-opacity="0.2"/>
      </linearGradient>
      <linearGradient id="shard-side" x1="1" y1="0" x2="0" y2="1">
        <stop offset="0" stop-color="#f16a92"/>
        <stop offset="1" stop-color="#fbd0dc" stop-opacity="0.3"/>
      </linearGradient>
      <linearGradient id="shard-bottom" x1="0" y1="1" x2="1" y2="0">
        <stop offset="0" stop-color="#f2829f"/>
        <stop offset="1" stop-color="#fde3ea" stop-opacity="0.1"/>
      </linearGradient>
    </defs>
    <polygon points="0,0 300,0 0,230" fill="url(#shard-top)"/>
    <polygon points="0,0 560,0 300,95" fill="#fbd0dc" opacity="0.5"/>
    <polygon points="700,0 1200,0 1200,130 1000,90" fill="url(#shard-top)" opacity="0.7"/>
    <polygon points="1200,60 1200,480 1090,240" fill="url(#shard-side)"/>
    <polygon points="1200,300 1200,925 1090,925 1150,600" fill="url(#shard-side)" opacity="0.6"/>
    <polygon points="0,650 140,925 0,925" fill="url(#shard-bottom)"/>
    <polygon points="0,760 420,925 0,925" fill="#fbd0dc" opacity="0.5"/>
    <polygon points="820,925 1200,780 1200,925" fill="url(#shard-bottom)" opacity="0.7"/>
  </svg>

  <svg class="award-ribbon" width="148" height="226" viewBox="0 0 148 226" aria-hidden="true">
    <polygon points="0,0 148,0 148,226 74,180 0,226" fill="var(--crimson)"/>
    <circle cx="75" cy="91" r="50" fill="var(--paper)"/>
    <circle cx="75" cy="91" r="40" fill="none" stroke="var(--purple)" stroke-width="5"/>
  </svg>

  <h1 class="club-title">THE AERIAL<br>CARTWHEEL CLUB</h1>

  <div class="skill-illustration" role="img" aria-label="Illustration of a gymnast performing an aerial cartwheel in five stages"></div>
  <div class="ground-line"></div>

  <div class="presented-band">THIS CERTIFICATE IS PROUDLY PRESENTED TO</div>

  <p class="gymnast-name">Mia Carter</p>
  <div class="name-rule"></div>
  <p class="award-details">by Gymnastics Gym on February 28, 2017</p>

  <p class="gym-logo">Gym Logo</p>

  <div class="brand-mark">
    <span class="brand-dot"></span>
    <span class="brand-name">TUMBLENEST</span>
  </div>
</main>
</body>
</html>
```